wardrobe/costume stylist needs good business card for own business

Hi:)

I'm wanting a business card for my company. I am a freelance stylist.

I do wardrobe/costume stylist to TV commercials; Films; Fashion and Lifestyle shoots.

I'd like a design based around my name Rosalind Darby written nicely, maybe a colour? Up to you?!

I've attached a couple of images of business cards I like
.... be creative and have fun!

Thank you :)
Updates

Reason: I was trying to get my new business card ready for before I headed overseas Friday morning but I don't think that was realistic so I'd like to extend the deadline to give time to the project. Thank you

Hi designers:) Thank you for all your designs, I've extended the deadline until Sunday, so there's a bit more time. I've attached 3 pictures of business cards which I quite like, please take a look to see if it can be of help in your process. I like the pale plain or patterned background with dark font and the dark plain or patterned background with the pale font the motifs the feminine fonts the plain fonts I like the idea of playing with a circle or some shape on one side of the card with my name or initials as in the picture I have on my post could you play around with this idea a bit please? Thank you all for the work you've done :) Rosie

Hi I am working overseas til Saturday night sorry for no feedback until I teturn Thanks :) Rosie

Hi designers, Thank you all so much for submitting your designs, I really appreciate your input into my project :) I'm sorry I didn't get to respond to some comments, and give feedback. I didn't back from being away until later than I expected, and the deadline had passed then, so apologies. Thanks to you all again for all your really good designs :) Rosie

Target Market(s)

I am a freelance stylist my target audience is producers, production companies, photographers, directors...

Industry/Entity Type

Business

Requirements
Must have
• Rosalind Darby
Stylist or Wardrobe Stylist

email rosiedarby@mailpeak.co.nz
Mobile 0218846193

(Don't have to use the words 'email' and 'mobile')
Nice to have
• Would like it to be double sided
Like B & W
Like pale colour background with dark font or white font
Like dark colour background with pale font
Should not have
• I would prefer it not to incorporate pictures

```html
<!DOCTYPE html>
<html lang="en">
<head>
<meta charset="utf-8">
<title>Rosalind Darby – Business Card</title>
<link rel="stylesheet" href="https://fonts.googleapis.com/css2?family=IM+Fell+English+SC&family=Cormorant+Garamond:wght@500&family=Open+Sans:wght@400&display=swap">
<style>
  :root {
    --backdrop: #d6d6d6;
    --card-dark: #645252;
    --card-pale: #fdf0e6;
    --seal: #c6aba1;
    --ink: #6b5552;
    --ink-soft: #7d6a66;
    --flourish-a: rgba(198, 171, 161, 0.35);
    --flourish-b: rgba(198, 171, 161, 0);
  }
  * { margin: 0; padding: 0; box-sizing: border-box; }
  html, body {
    width: 1200px;
    height: 655px;
    overflow: hidden;
    background: var(--backdrop);
  }
  .canvas {
    position: relative;
    width: 1200px;
    height: 655px;
  }
  .card {
    position: absolute;
    left: 207px;
    top: 212px;
    width: 786px;
    height: 229px;
    display: flex;
  }
  .card-front {
    width: 393px;
    height: 100%;
    background: var(--card-dark);
    display: flex;
    align-items: center;
    justify-content: center;
  }
  .seal {
    width: 134px;
    height: 134px;
    border-radius: 50%;
    background: var(--seal);
    display: flex;
    align-items: center;
    justify-content: center;
    text-align: center;
    margin-top: -4px;
  }
  .seal-name {
    font-family: "IM Fell English SC", serif;
    font-size: 17px;
    line-height: 1.15;
    color: var(--card-dark);
  }
  .card-back {
    position: relative;
    width: 393px;
    height: 100%;
    background: var(--card-pale);
  }
  .name-flourish {
    position: absolute;
    left: 40px;
    top: 70px;
    width: 313px;
    height: 92px;
    border-radius: 46px;
    background: radial-gradient(ellipse at center, var(--flourish-a), var(--flourish-b) 70%);
  }
  .name {
    position: absolute;
    left: 0;
    top: 92px;
    width: 100%;
    text-align: center;
    font-family: "IM Fell English SC", serif;
    font-size: 38px;
    line-height: 1;
    color: var(--ink);
    letter-spacing: 0.5px;
  }
  .role {
    position: absolute;
    left: 50px;
    top: 180px;
    width: 293px;
    display: flex;
    align-items: center;
    gap: 6px;
    font-family: "Cormorant Garamond", serif;
    font-weight: 500;
    font-size: 13px;
    color: var(--ink-soft);
    letter-spacing: 0.4px;
    white-space: nowrap;
  }
  .role-rule {
    flex: 1;
    height: 1px;
    background: var(--ink-soft);
  }
  .contact {
    position: absolute;
    left: 0;
    top: 199px;
    width: 100%;
    text-align: center;
    font-family: "Open Sans", sans-serif;
    font-size: 10px;
    color: var(--ink);
  }
</style>
</head>
<body>
<main class="canvas">
  <section class="card">
    <div class="card-front">
      <div class="seal">
        <span class="seal-name">Rosalind<br>Darby</span>
      </div>
    </div>
    <div class="card-back">
      <div class="name-flourish" role="img" aria-label="Decorative scrolling flourishes framing the name"></div>
      <h1 class="name">Rosalind Darby</h1>
      <p class="role"><span class="role-rule"></span>STYLIST OR WARDROBE STYLIST<span class="role-rule"></span></p>
      <p class="contact">rosiedarby@mailpeak.co.nz | 0218846193</p>
    </div>
  </section>
</main>
</body>
</html>
```